Website Design for Australian Vocational Education organisation

A website for an Educational organisation. A responsive design that works well on a laptop desktop or a mobile phone. Is easy to navigate. Be able to start small and add new pages and features at a later stage.
Requires the logo, the name of company, home page with hero shots, enquiry form that forwards to a specified email address
links to social media, home page. We need a home page, and two more templates for sub pages.
Must not be a typical common design.

current website www.qvtl.edu.au
this needs to look different. logo should remain the same.

Target Market(s)

across age groups from 18-70. so must be inutitive. some will be tech savvy and others not.

Industry/Entity Type

Education

Coding

Coded - Design and coding required

Colors

Designer to choose colors to be used in the design.

Requirements
Must have
• responsive design, video, photo gallery, hero image, social media links, news feed, calendar, shopping cart, enquiry form
Nice to have
• Sample website
• www.bluegumlearning.com.au
• but should not be similar to this. it must look different. the sample is to give an idea on the various pages and links that will be required

```html
<!DOCTYPE html>
<html lang="en">
<head>
<meta charset="utf-8">
<title>Coastal Institute of Applied Skills</title>
<link rel="stylesheet" href="https://fonts.googleapis.com/css2?family=Montserrat:wght@300;400;500;600;700&family=Poppins:wght@400;600;700&display=swap">
<style>
  :root {
    --red: #e31d2f;
    --red-dark: #b5111f;
    --red-deep: #a10e1b;
    --yellow: #fdbb31;
    --navy: #1f2c6b;
    --cyan: #32c7f4;
    --white: #ffffff;
    --ink: #3a3a3a;
    --muted: #9a9a9a;
    --line: #e4e4e4;
  }
  * { margin: 0; padding: 0; box-sizing: border-box; }
  html, body { width: 1200px; height: 608px; overflow: hidden; background: var(--white); }
  body { font-family: "Montserrat", sans-serif; color: var(--white); position: relative; }

  .site-header { position: absolute; top: 0; left: 0; width: 1200px; height: 66px; background: var(--red); }
  .site-header .brand-panel { position: absolute; top: 0; left: 0; width: 1200px; height: 66px; }
  .brand { position: absolute; left: 210px; top: 6px; display: flex; align-items: center; gap: 8px; }
  .brand-square { width: 52px; height: 52px; background: var(--navy); }
  .brand-name { font-family: "Montserrat", sans-serif; font-weight: 700; font-size: 11px; line-height: 13px; color: var(--red); text-transform: uppercase; width: 92px; }

  .main-nav { position: absolute; left: 0; top: 0; width: 1200px; height: 66px; }
  .main-nav a { position: absolute; top: 31px; color: var(--white); text-decoration: none; font-size: 9.5px; font-weight: 500; line-height: 12px; white-space: nowrap; }
  .main-nav a.active::after { content: ""; position: absolute; left: 0; right: 0; bottom: -6px; height: 2px; background: var(--white); }
  .nav-home { left: 414px; }
  .nav-about { left: 470px; }
  .nav-courses { left: 531px; }
  .nav-students { left: 604px; }
  .nav-blog { left: 682px; }
  .nav-apply { left: 735px; }
  .nav-contact { left: 829px; }

  .header-tools { position: absolute; left: 901px; top: 25px; display: flex; gap: 8px; }
  .tool { width: 25px; height: 25px; border-radius: 50%; background: var(--red-deep); display: flex; align-items: center; justify-content: center; }

  .info-bar { position: absolute; top: 66px; left: 0; width: 1200px; height: 24px; background: var(--yellow); display: flex; align-items: center; justify-content: flex-end; padding-right: 213px; font-size: 10px; font-weight: 500; gap: 14px; }
  .info-bar span { display: flex; align-items: center; gap: 6px; }

  .hero { position: absolute; top: 90px; left: 0; width: 1200px; height: 437px; text-align: center; }
  .hero-photo { position: absolute; inset: 0; background: linear-gradient(100deg, #2f3a26 0%, #4d5546 30%, #5b5650 55%, #454a3e 80%, #2c3426 100%); }
  .hero-shade { position: absolute; inset: 0; background: rgba(0,0,0,0.28); }
  .hero-content { position: relative; padding-top: 150px; }
  .hero-kicker { font-size: 28px; font-weight: 300; letter-spacing: 0.5px; line-height: 36px; }
  .hero-title { font-size: 44px; font-weight: 700; letter-spacing: 1px; line-height: 56px; margin-top: 4px; }
  .hero-text { font-size: 13px; line-height: 18px; width: 680px; margin: 14px auto 0; font-weight: 400; }
  .hero-actions { margin-top: 42px; display: flex; justify-content: center; gap: 13px; }
  .btn { width: 143px; height: 34px; display: flex; align-items: center; justify-content: center; font-size: 11px; font-weight: 500; color: var(--white); text-decoration: none; }
  .btn-primary { background: var(--cyan); }
  .btn-outline { border: 1.5px solid var(--white); }

  .course-search { position: absolute; top: 527px; left: 0; width: 1200px; height: 81px; background: var(--red); }
  .course-search .band { position: absolute; inset: 0; }
  .search-label { position: absolute; left: 218px; top: 24px; font-family: "Poppins", sans-serif; text-align: center; }
  .search-label small { display: block; font-size: 13px; letter-spacing: 0.6px; line-height: 14px; }
  .search-label strong { display: block; font-size: 17px; font-weight: 700; letter-spacing: 1.5px; line-height: 20px; }
  .search-form { position: absolute; left: 395px; top: 26px; width: 557px; height: 30px; display: flex; background: var(--white); }
  .search-category { width: 129px; border-right: 1px solid var(--line); display: flex; align-items: center; justify-content: space-between; padding: 0 14px 0 24px; font-size: 9px; color: var(--ink); font-weight: 500; }
  .search-input { flex: 1; display: flex; align-items: center; padding-left: 17px; font-size: 8.5px; color: var(--muted); }
  .search-submit { width: 34px; background: var(--navy); display: flex; align-items: center; justify-content: center; }
</style>
</head>
<body>
  <header class="site-header">
    <svg class="brand-panel" width="1200" height="66" aria-hidden="true">
      <polygon points="0,0 405,0 385,66 0,66" fill="#ffffff"/>
    </svg>
    <div class="brand">
      <div class="brand-square"></div>
      <div class="brand-name">Coastal Institute of Applied Skills</div>
    </div>
    <nav class="main-nav">
      <a class="nav-home active" href="#">HOME</a>
      <a class="nav-about" href="#">ABOUT</a>
      <a class="nav-courses" href="#">COURSES</a>
      <a class="nav-students" href="#">STUDENTS</a>
      <a class="nav-blog" href="#">BLOG</a>
      <a class="nav-apply" href="#">APPLY ONLINE</a>
      <a class="nav-contact" href="#">CONTACT</a>
    </nav>
    <div class="header-tools">
      <span class="tool"><svg width="10" height="10" viewBox="0 0 10 10"><circle cx="4" cy="4" r="3" fill="none" stroke="#fff" stroke-width="1.6"/><line x1="6.2" y1="6.2" x2="9" y2="9" stroke="#fff" stroke-width="1.8"/></svg></span>
      <span class="tool"><svg width="10" height="10" viewBox="0 0 10 10"><circle cx="5" cy="3" r="2.3" fill="#fff"/><path d="M1 10 Q1 5.5 5 5.5 Q9 5.5 9 10Z" fill="#fff"/></svg></span>
      <span class="tool"><svg width="10" height="11" viewBox="0 0 10 11"><path d="M3 4 V2.5 Q5 0 7 2.5 V4" fill="none" stroke="#fff" stroke-width="1.2"/><rect x="1" y="3.5" width="8" height="7" rx="1" fill="#fff"/></svg></span>
    </div>
  </header>

  <div class="info-bar">
    <span><svg width="11" height="10" viewBox="0 0 11 10"><path d="M0 4.5 L11 0 L7 10 L5 6 Z" fill="#fff"/></svg>INFO@CIAS.EDU.AU</span>
    <span>|</span>
    <span><svg width="10" height="10" viewBox="0 0 10 10"><circle cx="5" cy="5" r="4.2" fill="none" stroke="#fff" stroke-width="1.2"/><path d="M5 2.5 V5 H7" fill="none" stroke="#fff" stroke-width="1.1"/></svg>MON - SAT : 9:00 -18:00</span>
  </div>

  <section class="hero">
    <div class="hero-photo" role="img" aria-label="Photo of four smiling students sitting on the grass outdoors with notebooks"></div>
    <div class="hero-shade"></div>
    <div class="hero-content">
      <p class="hero-kicker">MEET NEW FRIENDS</p>
      <h1 class="hero-title">STUDY WITH EXPERTS</h1>
      <p class="hero-text">Lorem ipsum dolor sit amet, consectetur adipiscing elit. Donec et velit ipsum. Fusce luctus eget ex nec vehicula. Phasellus eu ultrices metus, feugiat porta nulla.</p>
      <div class="hero-actions">
        <a class="btn btn-primary" href="#">VIEW COURSES</a>
        <a class="btn btn-outline" href="#">APPLY ONLINE</a>
      </div>
    </div>
  </section>

  <section class="course-search">
    <svg class="band" width="1200" height="81" aria-hidden="true">
      <polygon points="0,0 320,0 366,81 0,81" fill="#b5111f"/>
    </svg>
    <div class="search-label"><small>SEARCH FOR</small><strong>COURSES</strong></div>
    <div class="search-form">
      <div class="search-category">ALL CATEGORIES <svg width="7" height="5" viewBox="0 0 7 5"><path d="M0.5 0.8 L3.5 3.8 L6.5 0.8" fill="none" stroke="#777" stroke-width="1"/></svg></div>
      <div class="search-input">ENTER COURSE NAME</div>
      <div class="search-submit"><svg width="12" height="12" viewBox="0 0 10 10"><circle cx="4" cy="4" r="3" fill="none" stroke="#fff" stroke-width="1.6"/><line x1="6.2" y1="6.2" x2="9" y2="9" stroke="#fff" stroke-width="1.8"/></svg></div>
    </div>
  </section>
</body>
</html>
```